Attention grabbing 6x9 postcard

We are looking to have an attention grabbing post card that be sent out to homeowners from our roofing company Olum Roofing. the concept is that on the front it will say something like (STOP THE KNOCKING!
Tired of roofers knocking on your door? Contact us because we value your time as much as you value the roof over your head."
Olum Roofing
OlumRoofing.com
877.612.OLUM
info@olumroofing.com

Please feel free to come up with something very creative. Once we pick the final design we will provide the copy.

```html
<!DOCTYPE html>
<html lang="en">
<head>
<meta charset="utf-8">
<title>Olum Roofing – Stop the Knocking Postcard</title>
<link rel="stylesheet" href="https://fonts.googleapis.com/css2?family=Jost:wght@500;600&family=Poppins:wght@400;600;700;800&family=Montserrat:wght@400&display=swap">
<style>
  :root {
    --ink: #070707;
    --honey: #e8b23a;
    --paper: #ffffff;
    --navy: #2b4d9c;
    --roof-dark: #4e5359;
    --roof-mid: #6c7077;
    --brick: #a87468;
    --lawn: #6d9a3f;
  }
  * { margin: 0; padding: 0; box-sizing: border-box; }
  html, body { width: 1200px; height: 883px; overflow: hidden; background: var(--paper); }
  .postcard { position: relative; width: 1200px; height: 883px; background: var(--ink); overflow: hidden; }

  .header { position: absolute; left: 0; top: 0; width: 1200px; height: 272px; background: var(--ink); }
  .brand { position: absolute; left: 56px; top: 72px; display: flex; align-items: center; gap: 34px; }
  .brand-mark { width: 118px; height: 118px; border-radius: 50%; background: var(--honey); flex: none; }
  .brand-name { font-family: "Jost", sans-serif; font-weight: 600; color: var(--paper); font-size: 70px; line-height: 78px; letter-spacing: 0.12em; }

  .headline { position: absolute; left: 690px; top: 60px; width: 420px; text-align: center; font-family: "Poppins", sans-serif; font-weight: 800; line-height: 1; letter-spacing: 0.04em; }
  .headline .line-one { display: block; color: var(--honey); font-size: 66px; }
  .headline .line-two { display: block; color: var(--paper); font-size: 70px; margin-top: 10px; }
  .tagline { position: absolute; left: 690px; top: 224px; width: 420px; text-align: center; font-family: "Poppins", sans-serif; font-weight: 600; font-size: 16.5px; color: var(--paper); }

  .honey-band { position: absolute; left: 0; top: 272px; width: 1200px; height: 42px; background: var(--honey); }

  .house-photo { position: absolute; left: 0; top: 314px; width: 1200px; height: 428px;
    background: linear-gradient(100deg, var(--roof-mid) 0%, var(--roof-dark) 30%, var(--brick) 55%, #c9b2a8 72%, var(--lawn) 95%); }

  .services-frame { position: absolute; left: 681px; top: 314px; width: 438px; height: 405px; background: var(--honey); }
  .services { position: absolute; left: 704px; top: 314px; width: 391px; height: 378px; background: var(--paper); list-style: none; }
  .service { position: absolute; left: 33px; display: flex; align-items: center; gap: 20px; }
  .service-icon { width: 51px; height: 60px; flex: none; }
  .service-label { font-family: "Poppins", sans-serif; font-weight: 400; font-size: 17.5px; line-height: 24px; letter-spacing: 0.22em; color: var(--ink); }

  .footer { position: absolute; left: 0; top: 742px; width: 1200px; height: 141px; background: var(--ink); }
  .promise { position: absolute; left: 59px; top: 30px; padding-left: 21px; border-left: 9px solid var(--honey); font-family: "Montserrat", sans-serif; font-size: 17px; line-height: 22px; color: var(--paper); width: 330px; }
  .contact { position: absolute; left: 413px; top: 24px; list-style: none; font-family: "Montserrat", sans-serif; font-size: 21.5px; color: var(--paper); }
  .contact li { display: flex; align-items: center; gap: 12px; height: 42px; }
  .contact svg { width: 24px; height: 24px; flex: none; }
  .phone { position: absolute; left: 745px; top: 42px; display: flex; align-items: center; gap: 18px; font-family: "Poppins", sans-serif; font-weight: 700; font-size: 38px; color: var(--paper); letter-spacing: 0.01em; }
  .phone svg { width: 42px; height: 42px; flex: none; }
</style>
</head>
<body>
<div class="postcard">
  <header class="header">
    <div class="brand">
      <span class="brand-mark"></span>
      <div class="brand-name">OLUM<br>ROOFING</div>
    </div>
    <h1 class="headline"><span class="line-one">STOP THE</span><span class="line-two">KNOCKING!</span></h1>
    <p class="tagline">Tired of roofers knocking on your door?</p>
  </header>

  <div class="honey-band"></div>

  <div class="house-photo" role="img" aria-label="Aerial view of a brick house with a grey shingle roof and green lawn"></div>

  <div class="services-frame"></div>
  <ul class="services">
    <li class="service" style="top:32px">
      <svg class="service-icon" viewBox="0 0 51 60"><polygon points="25.5,2 49,15.5 49,44.5 25.5,58 2,44.5 2,15.5" fill="var(--honey)" stroke="var(--navy)" stroke-width="2.5"/><polyline points="14,31 22,39 37,21" fill="none" stroke="var(--ink)" stroke-width="5"/></svg>
      <span class="service-label">RETAIL/COMMERCIAL<br>ROOF REPLACEMENT</span>
    </li>
    <li class="service" style="top:116px">
      <svg class="service-icon" viewBox="0 0 51 60"><polygon points="25.5,2 49,15.5 49,44.5 25.5,58 2,44.5 2,15.5" fill="var(--honey)" stroke="var(--navy)" stroke-width="2.5"/><polyline points="14,31 22,39 37,21" fill="none" stroke="var(--ink)" stroke-width="5"/></svg>
      <span class="service-label">STORM DAMAGE<br>ROOF REPLACEMENT</span>
    </li>
    <li class="service" style="top:200px">
      <svg class="service-icon" viewBox="0 0 51 60"><polygon points="25.5,2 49,15.5 49,44.5 25.5,58 2,44.5 2,15.5" fill="var(--honey)" stroke="var(--navy)" stroke-width="2.5"/><polyline points="14,31 22,39 37,21" fill="none" stroke="var(--ink)" stroke-width="5"/></svg>
      <span class="service-label">NEW<br>CONSTRUCTION</span>
    </li>
    <li class="service" style="top:283px">
      <svg class="service-icon" viewBox="0 0 51 60"><polygon points="25.5,2 49,15.5 49,44.5 25.5,58 2,44.5 2,15.5" fill="var(--honey)" stroke="var(--navy)" stroke-width="2.5"/><polyline points="14,31 22,39 37,21" fill="none" stroke="var(--ink)" stroke-width="5"/></svg>
      <span class="service-label">REPAIRS &amp;<br>RESTORATION</span>
    </li>
  </ul>

  <footer class="footer">
    <p class="promise">Contact us because we value your time as much as you value the roof over your head.</p>
    <ul class="contact">
      <li>
        <svg viewBox="0 0 24 24" fill="none" stroke="var(--honey)" stroke-width="1.6"><circle cx="12" cy="12" r="10.5"/><ellipse cx="12" cy="12" rx="4.5" ry="10.5"/><line x1="1.5" y1="12" x2="22.5" y2="12"/><path d="M3.5 6.5h17M3.5 17.5h17"/></svg>
        <span>OlumRoofing.com</span>
      </li>
      <li>
        <svg viewBox="0 0 24 24" fill="none" stroke="var(--honey)" stroke-width="1.6"><circle cx="12" cy="12" r="10.5"/><rect x="6.5" y="8" width="11" height="8" rx="1"/><polyline points="6.5,8.5 12,13 17.5,8.5"/></svg>
        <span>info@olumroofing.com</span>
      </li>
    </ul>
    <div class="phone">
      <svg viewBox="0 0 42 42"><circle cx="21" cy="21" r="18.5" fill="none" stroke="var(--honey)" stroke-width="4"/><path d="M14.5 11.5l4 0 1.8 5-2.6 2a12 12 0 0 0 5.8 5.8l2-2.6 5 1.8v4c0 1.2-1 2-2.2 2A17 17 0 0 1 12.5 13.7c0-1.2.8-2.2 2-2.2z" fill="var(--honey)"/></svg>
      <span>877.612.OLUM</span>
    </div>
  </footer>
</div>
</body>
</html>
```